Bakersfield's Grand Dash 2015 POSTER

Looking for a hip design to attract young 20-30 somethings to a downtown scavenger hunt as a benefit for a local non-profit. Please see our website at www.granddashfun.org. Race Date is March 14, 2015, in Downtown Bakersfield.

```html
<!DOCTYPE html>
<html lang="en">
<head>
<meta charset="utf-8">
<title>Bakersfield's Grand Dash 2015 Poster</title>
<link rel="stylesheet" href="https://fonts.googleapis.com/css2?family=Lato:ital,wght@0,300;0,400;0,700;0,900;1,700&family=Lobster+Two:ital,wght@1,700&family=Arimo:wght@700&display=swap">
<style>
  :root {
    --stage: #ebe8e3;
    --paper: #fbfbfb;
    --photo-light: #cfcfcf;
    --photo-dark: #7d7d7d;
    --purple: #7b2fa8;
    --magenta: #b23ec4;
    --orange: #d8431c;
    --blue: #1d3fa5;
    --pill-blue: #2f7fb8;
    --red: #e3151a;
    --yellow: #f4d21f;
    --teal: #1aa6b0;
    --green: #168a2f;
    --ink: #2a2a2a;
  }
  * { margin: 0; padding: 0; box-sizing: border-box; }
  html, body { width: 903px; height: 1200px; overflow: hidden; background: var(--stage); }
  .poster {
    position: absolute; left: 66px; top: 56px; width: 770px; height: 1078px;
    background: var(--paper); overflow: hidden;
    box-shadow: 0 2px 8px rgba(0,0,0,.18);
    font-family: "Lato", sans-serif;
  }
  .street-photo {
    position: absolute; left: 0; top: 0; width: 770px; height: 600px;
    background: linear-gradient(180deg, var(--photo-light) 0%, #a9a9a9 45%, var(--photo-dark) 70%, #bdbdbd 100%);
  }
  .snapshot { position: absolute; border: 5px solid #fff; box-shadow: 1px 2px 5px rgba(0,0,0,.35); }
  .snapshot-team { left: 84px; top: 96px; width: 225px; height: 130px; transform: rotate(3deg); background: linear-gradient(135deg, #c9a982, #6b5a4a); }
  .snapshot-runners { left: 26px; top: 240px; width: 180px; height: 160px; transform: rotate(3deg); background: linear-gradient(135deg, #b7b2a8, #4d4f55); }
  .snapshot-bowling { left: 167px; top: 212px; width: 235px; height: 152px; transform: rotate(-4deg); background: linear-gradient(135deg, #9fc3d6, #c7a468); }
  .social-link {
    position: absolute; right: 18px; top: 30px; display: flex; align-items: center; gap: 5px;
    font-weight: 700; font-size: 13px; color: #fff;
  }
  .social-link::before { content: ""; width: 14px; height: 14px; background: #3b5a9a; }
  .waves { position: absolute; left: 0; top: 490px; width: 770px; height: 170px; }
  .event-date {
    position: absolute; left: 24px; top: 668px;
    font-family: "Lobster Two", cursive; font-style: italic; font-weight: 700;
    font-size: 50px; color: var(--purple); letter-spacing: .5px;
  }
  .event-place { position: absolute; left: 24px; top: 728px; font-weight: 900; font-size: 30px; color: var(--orange); }
  .about-pill {
    position: absolute; left: 0; top: 787px; width: 364px; height: 47px;
    background: linear-gradient(180deg, #4ea0d6, var(--pill-blue));
    border-radius: 0 24px 24px 0; color: #fff;
    font-weight: 700; font-size: 27px; line-height: 47px; padding-left: 22px;
  }
  .about-text {
    position: absolute; left: 12px; top: 854px; width: 746px;
    font-size: 15.2px; line-height: 20px; color: var(--ink); text-align: justify;
  }
  .race-brand { position: absolute; left: 434px; top: 572px; width: 300px; height: 272px; text-align: center; }
  .race-brand > * { position: absolute; left: 0; width: 300px; }
  .skyline-art {
    top: 0; left: 30px !important; width: 240px !important; height: 64px;
    background: linear-gradient(90deg, #d98bd6, #8fa4e0, #7cc7c4, #c98ad7); opacity: .85;
  }
  .brand-place { top: 62px; font-weight: 700; font-style: italic; font-size: 18px; line-height: 20px; color: var(--magenta); }
  .brand-name {
    top: 82px; font-weight: 300; color: var(--magenta); font-size: 50px; line-height: 50px; letter-spacing: 4px;
  }
  .tagline { top: 190px; font-weight: 700; font-style: italic; color: var(--teal); font-size: 17px; line-height: 20px; }
  .register {
    top: 216px; font-family: "Arimo", sans-serif; font-weight: 700; color: var(--green);
    font-size: 46px; line-height: 52px; letter-spacing: -.5px; white-space: nowrap;
  }
  .web-band {
    position: absolute; left: 0; top: 929px; width: 770px; height: 44px;
    background: var(--red); border-bottom: 5px solid var(--yellow);
    color: #fff; font-weight: 700; font-size: 30px; text-align: center; line-height: 44px;
    box-sizing: content-box;
  }
  .sponsors {
    position: absolute; left: 10px; top: 1000px; width: 750px; height: 60px;
    display: flex; justify-content: space-between; align-items: center;
  }
  .sponsor { font-weight: 700; font-size: 13px; color: #333; display: flex; align-items: center; gap: 5px; }
  .sponsor .mark { width: 12px; height: 12px; background: var(--red); }
  .sponsor .mark.round { border-radius: 50%; }
  .sponsor .mark.navy { background: var(--blue); }
</style>
</head>
<body>
<main class="poster">
  <div class="street-photo" role="img" aria-label="Black and white photo of a downtown Bakersfield street corner with a tall office building and traffic lights"></div>
  <div class="snapshot snapshot-team" role="img" aria-label="Photo of a race team posing together indoors"></div>
  <div class="snapshot snapshot-runners" role="img" aria-label="Photo of two racers wearing race numbers"></div>
  <div class="snapshot snapshot-bowling" role="img" aria-label="Photo of teams at a bowling alley holding a Bakersfield sign"></div>
  <div class="social-link">Linkup</div>

  <svg class="waves" viewBox="0 0 770 170" aria-hidden="true">
    <path d="M0 20 C200 130 420 120 770 10 L770 170 L0 170 Z" fill="var(--paper)"/>
    <path d="M0 20 C180 110 380 80 770 30 L770 60 C430 80 230 140 0 70 Z" fill="var(--blue)"/>
    <path d="M0 60 C210 130 400 95 770 45 L770 58 C420 95 220 150 0 80 Z" fill="var(--yellow)"/>
    <path d="M0 80 C230 160 440 110 770 60 L770 130 C480 95 270 175 0 100 Z" fill="var(--red)"/>
    <path d="M0 20 C170 95 360 70 770 15 L770 35 C390 75 200 120 0 50 Z" fill="var(--magenta)"/>
    <path d="M0 100 C270 175 480 100 770 130 L770 170 L0 170 Z" fill="var(--paper)"/>
  </svg>

  <div class="event-date">March 14, 2015</div>
  <div class="event-place">Downtown Bakersfield</div>

  <section class="race-brand">
    <div class="skyline-art" role="img" aria-label="Colorful illustrated skyline of downtown Bakersfield landmarks"></div>
    <div class="brand-place">Bakersfield's</div>
    <div class="brand-name">GRAND<br>DASH</div>
    <div class="tagline">Test your city limits!</div>
    <div class="register">Register now</div>
  </section>

  <h2 class="about-pill">About Grand Dash</h2>
  <p class="about-text">The Bakersfield Grand Dash is an annual race that is part scavenger hunt and part obstacle course. Teams of 2-4 will solve twelve clues and complete various mental and physical challenges in downtown Bakersfield. Contestants will experience the best that downtown Bakersfield has to offer in a whole new way.</p>

  <div class="web-band">www.granddashfun.org</div>

  <footer class="sponsors">
    <span class="sponsor"><span class="mark round"></span>Core District Assoc.</span>
    <span class="sponsor">BrightWire USA</span>
    <span class="sponsor"><span class="mark navy"></span>WAVE 98.1</span>
    <span class="sponsor">Unity Health</span>
    <span class="sponsor">Ridge Peak Resort</span>
    <span class="sponsor">Harlan Reed Law</span>
  </footer>
</main>
</body>
</html>
```